Rioja winery needs a new label design

A family-owned winery in Spain's Rioja Oriental region is looking to create a new label for a wine named "Zunad" Arabic for Castle, that reflects the land from which the wine is born. From the remote village of Quel, La Rioja Oriental, with the backdrop of the Sierra Yerga mountains and the Barrio de Bodegas, or group of caves where locals have produced wines for centuries. Wine name:
2018 Zunad Rioja Tempranillo
Quel, Rioja Oriental
Spain

Font styles to use
Serif
Sans Serif
Decorative
Script

Requirements
Must have
• vines, vineyards, grapes
Nice to have
• mountains,
Should not have
• castles. we already have a label design with the castle

```html
<!DOCTYPE html>
<html lang="en">
<head>
<meta charset="UTF-8">
<title>Zunad 2018 Rioja Tempranillo – Label</title>
<link href="https://fonts.googleapis.com/css2?family=Cinzel:wght@400;500&family=Josefin+Sans:wght@300;400&family=Raleway:wght@200&display=swap" rel="stylesheet">
<style>
  :root {
    --page: #ffffff;
    --label-black: #111111;
    --wordmark-grey: #5a5a5a;
    --year-grey: #4a4a4a;
    --ridge-grey: #6a6a6a;
    --gold: #c9b23c;
    --ink-light: #f2f2f2;
  }
  * { margin: 0; padding: 0; box-sizing: border-box; }
  html, body {
    width: 1200px;
    height: 1127px;
    overflow: hidden;
    background: var(--page);
  }
  .label {
    position: absolute;
    left: 218px;
    top: 24px;
    width: 763px;
    height: 1078px;
    background: var(--label-black);
    color: var(--ink-light);
  }
  .mountain-ridge {
    position: absolute;
    left: 90px;
    top: 108px;
    width: 572px;
    height: 64px;
    background: linear-gradient(180deg, rgba(106,106,106,0) 0%, rgba(106,106,106,0.28) 55%, rgba(106,106,106,0) 100%);
  }
  .vertical-type {
    position: absolute;
    left: 0;
    top: 0;
    width: 763px;
    height: 760px;
  }
  .wordmark {
    font-family: "Cinzel", serif;
    font-weight: 400;
    fill: var(--wordmark-grey);
  }
  .vintage {
    font-family: "Raleway", sans-serif;
    font-weight: 200;
    fill: var(--year-grey);
  }
  .varietal {
    position: absolute;
    left: 0;
    top: 722px;
    width: 763px;
    text-align: center;
    font-family: "Cinzel", serif;
    font-size: 38px;
    letter-spacing: 3px;
    color: var(--gold);
  }
  .facts {
    position: absolute;
    left: 0;
    top: 866px;
    width: 763px;
    font-family: "Cinzel", serif;
    color: var(--ink-light);
  }
  .facts .volume,
  .facts .strength {
    position: absolute;
    top: 16px;
    font-size: 17px;
  }
  .facts .volume { left: 58px; }
  .facts .strength { right: 52px; }
  .facts .origin {
    position: absolute;
    left: 0;
    width: 763px;
    text-align: center;
    font-size: 24px;
    line-height: 30px;
    letter-spacing: 0.5px;
  }
  .additional-info {
    position: absolute;
    left: 36px;
    top: 950px;
    width: 691px;
    text-align: center;
    font-family: "Josefin Sans", sans-serif;
    font-weight: 400;
    font-size: 17px;
    line-height: 23px;
    color: var(--ink-light);
  }
</style>
</head>
<body>
  <main class="label">
    <div class="mountain-ridge" role="img" aria-label="Line drawing of the Sierra Yerga mountain ridge"></div>

    <svg class="vertical-type" viewBox="0 0 763 760" aria-hidden="false">
      <text class="wordmark" transform="translate(426 706) rotate(-90)" font-size="170" textLength="480" lengthAdjust="spacingAndGlyphs">ZUNAD</text>
      <text class="vintage" transform="translate(298 468) rotate(-90)" font-size="82" textLength="242" lengthAdjust="spacing">2018</text>
    </svg>

    <h1 class="varietal">Rioja Tempranillo</h1>

    <section class="facts">
      <span class="volume">750 ml</span>
      <p class="origin">Quel, Rioja Oriental<br>Spain</p>
      <span class="strength">Alc 13% Vol.</span>
    </section>

    <p class="additional-info">Información adicional: Lorem ipsum dolor sit amet, consectetuer adipiscing elit. Aenean commodo ligula eget dolor. Aenean massa. Cum sociis natoque penatibus et magnis dis parturient montes, nascetur ridiculus mus.</p>
  </main>
</body>
</html>
```